Need a Wordpress website for my HVAC company

I need a Wordpress website created for an HVAC company in a competitive market.
Following are some websites I like:
My current website is www.brovikclimate.com - we also have a facebook page with some pictures

We are an airconditioning and heating company that does both residential and commmercial work.
We need the following info on our website:
-mobile friendly
-Schedule an appt -repair/maintnenace/installation (i would like this option to always be on the page even if they scroll down.)
-24 hour service
-coupons /promotions
-financing
-reviews/testimonials
-about
-blog
-Our service area
The following are services we provide:
-Air conditioning - Installation/Service/Maintenance/new construction
-Heating - Installation/Service/Maintenance/new construction ( gas furnace, 2 stage furnace, electric heat)
-Duct - Repair/Replacement/Istallation - (zone systems)
-thermostats (wifi)
-Heat pump
-Air handler
-self communicating systems
-carbon monoxide testing
-hail damage
-duct sealing
-insulation
-Air cleaners - UV Air purifiers
-humidifiers

I would also like Quillo SEO add on

Target Market(s)

Anyone who needs our services HVAC contractor

Industry/Entity Type

Hvac

Contact Information for Business Card

Phone:480-555-2064
website:www.brovikclimate.com
email pmarsh@brovikclimate.com

Coding

Coded - Design and coding required

Number of Pages Required

5+ page

Font styles to use
Serif
Sans Serif

Requirements
Must have
• I wrote in brief. I already have Nimbo Vault. Long story I paid for 3 years already. I need someone to put website there. Ive never used Wordpress but would like a template page so I can easily add services.
Nice to have
• Clean, bright, original

```html
<!DOCTYPE html>
<html lang="en">
<head>
<meta charset="utf-8">
<title>Brovik Climate Services</title>
<link rel="stylesheet" href="https://fonts.googleapis.com/css2?family=Open+Sans:wght@400;600;700;800&display=swap">
<style>
:root{
  --blue:#0d5a9e;
  --blue-dark:#0a4a85;
  --red:#c8202f;
  --green:#26923f;
  --ink:#333333;
  --muted:#555555;
  --grey-bg:#eeeeee;
  --footer:#2f2f2f;
  --footer-bar:#242424;
  --white:#ffffff;
}
*{box-sizing:border-box;margin:0;padding:0}
html,body{width:1200px;height:2866px;overflow:hidden}
body{font-family:"Open Sans",Arial,sans-serif;color:var(--ink);position:relative;background:var(--white)}
.abs{position:absolute}
/* top bar */
.topbar{left:0;top:0;width:1200px;height:29px;background:var(--blue)}
.topbar .welcome{left:157px;top:7px;font-size:11px;color:var(--white)}
.social{display:flex;gap:14px;right:150px;top:8px}
.social span{width:12px;height:12px;border-radius:50%;background:var(--white);opacity:.9;display:block}
/* header */
.brand-bump{left:550px;top:0;width:180px;height:150px;border-radius:0 0 90px 90px;background:var(--white)}
.brand{left:550px;top:34px;width:180px;text-align:center}
.brand .mark{width:60px;height:60px;border-radius:50%;background:var(--blue);margin:0 auto 8px}
.brand .name{font-size:17px;font-weight:800;color:var(--blue);line-height:1.15}
.contact-box{top:69px;height:54px;border:1px solid #bbb;display:flex;align-items:center;gap:12px;padding-left:14px;overflow:hidden;white-space:nowrap}
.contact-box .label{font-size:12px;font-weight:600;color:var(--blue)}
.contact-box .value{font-size:21px;font-weight:700;color:var(--red);line-height:1.1}
.contact-box.phone{left:157px;width:226px}
.contact-box.mail{left:789px;width:264px}
.contact-box.mail .value{font-size:16px}
/* nav */
.nav{left:0;top:157px;width:1200px;height:36px;background:var(--red)}
.nav ul{list-style:none;display:flex;gap:25px;position:absolute;left:157px;top:11px}
.nav li{font-size:11px;font-weight:700;color:var(--white)}
.search{left:1020px;top:157px;width:36px;height:36px;background:var(--green);display:flex;align-items:center;justify-content:center}
/* hero */
.hero{left:0;top:193px;width:1200px;height:451px;background:linear-gradient(135deg,#5d8fc0 0%,#3f77b2 45%,#6b9ac8 100%)}
.mascot{left:153px;top:55px;width:230px;height:364px;border-radius:40px;background:linear-gradient(180deg,#2f6fb5,#1d4f8a)}
.hero h1{left:411px;top:192px;font-size:30px;font-weight:600;color:var(--red)}
.hero .tag{left:402px;top:238px;font-size:13.5px;color:var(--white)}
.quick-form{left:787px;top:27px;width:268px;height:395px;background:var(--white);border:5px solid var(--blue)}
.quick-form h2{background:var(--red);color:var(--white);font-size:19px;font-weight:700;height:58px;line-height:58px;padding-left:16px}
.quick-form .intro{font-size:9px;color:#777;text-align:center;padding:14px 26px 0;line-height:1.4}
.field{position:absolute;left:19px;width:221px;height:28px;border:1px solid #aab;font-size:10px;color:#555;padding:6px 6px}
.submit{position:absolute;left:19px;top:323px;width:221px;height:33px;background:var(--blue);color:var(--white);font-size:11px;font-weight:700;text-align:center;line-height:33px}
/* section headings */
.sec-title{width:1200px;left:0;text-align:center;font-size:30px;font-weight:700;color:var(--red)}
.sec-title::after{content:"";display:block;width:105px;height:3px;background:var(--blue);margin:10px auto 0}
.sec-title.light{color:var(--white)}
.sec-title.light::after{background:var(--white)}
/* why */
.feature{width:270px}
.feature svg{display:block;margin-bottom:10px}
.feature h3{font-size:16px;font-weight:400;color:var(--ink);margin-bottom:14px}
.feature p{font-size:10.5px;line-height:1.75;color:var(--muted)}
/* services */
.services{left:0;top:1127px;width:1200px;height:627px;background:linear-gradient(180deg,#1d5fa3,#16548f)}
.card{width:269px;height:203px;background:var(--white)}
.card .photo{height:159px}
.card h3{font-size:16px;font-weight:700;color:#222;padding:12px 0 0 12px}
/* testimonials */
.review{width:372px;height:179px;border:1px solid #ddd;background:var(--white);padding:20px 20px 0 44px}
.review .who{font-size:12px;color:var(--red);display:inline-block;border-bottom:1px solid var(--red);padding-bottom:4px;margin-bottom:10px}
.review p{font-size:11px;line-height:1.75;color:var(--muted)}
.avatar{width:76px;height:76px;border-radius:50%;background:linear-gradient(180deg,#8b6b5a,#c9a58e);border:3px solid var(--white)}
/* cities */
.cities{left:0;top:2140px;width:1200px;height:445px;background:linear-gradient(180deg,#ececec,#e4e4e4)}
.cities .intro{left:159px;top:145px;width:395px;font-size:11px;line-height:1.7;color:var(--muted)}
.city-list{list-style:none;width:160px}
.city-list li{font-size:11px;height:30px;display:flex;align-items:center;gap:10px;color:#333}
.van{left:516px;top:134px;width:525px;height:239px;border-radius:30px 60px 20px 20px;background:linear-gradient(180deg,#f4f6f9,#2d64a8)}
/* footer */
.footer{left:0;top:2585px;width:1200px;height:251px;background:var(--footer)}
.footer h4{font-size:14px;font-weight:700;color:var(--white);margin-bottom:22px}
.footer p{font-size:10.5px;line-height:1.85;color:#ddd}
.links{list-style:none;font-size:10.5px;color:#ddd}
.links li{height:23px}
.links li::before{content:"›";margin-right:10px}
.f-social{display:flex;gap:16px}
.f-social span{width:10px;height:10px;border-radius:50%;background:#ddd;display:block}
.news-input{width:238px;height:31px;background:var(--white);font-size:10px;color:#999;padding:9px 10px;margin-top:22px}
.news-btn{width:238px;height:31px;background:var(--green);color:var(--white);font-size:13px;font-weight:700;text-align:center;line-height:31px;margin-top:9px}
.copy{left:0;top:2836px;width:1200px;height:30px;background:var(--footer-bar);color:#ddd;font-size:9.5px;text-align:center;line-height:30px}
.copy::before{content:"";position:absolute;left:157px;right:157px;top:0;height:1px;background:#777}
</style>
</head>
<body>

<header>
  <div class="abs topbar">
    <span class="abs welcome">Welcome to our Website</span>
    <div class="abs social"><span></span><span></span><span></span><span></span><span></span></div>
  </div>
  <div class="abs brand-bump"></div>
  <div class="abs brand">
    <div class="mark"></div>
    <div class="name">Brovik Climate</div>
  </div>
  <div class="abs contact-box phone">
    <svg width="26" height="26" viewBox="0 0 24 24" fill="none" stroke="#26923f" stroke-width="1.6"><path d="M5 3h4l2 5-2.5 1.5a11 11 0 0 0 6 6L16 13l5 2v4a2 2 0 0 1-2 2A16 16 0 0 1 3 5a2 2 0 0 1 2-2z"/></svg>
    <div><div class="label">Call Us 24/7 Hours</div><div class="value">(480) 555-2064</div></div>
  </div>
  <div class="abs contact-box mail">
    <svg width="28" height="22" viewBox="0 0 28 20" fill="none" stroke="#26923f" stroke-width="1.6"><rect x="1" y="1" width="26" height="18"/><path d="M1 1l13 10L27 1"/></svg>
    <div><div class="label">Contact with E-mail</div><div class="value">Info@brovikclimate.com</div></div>
  </div>
  <nav class="abs nav">
    <ul><li>HOME</li><li>ABOUT US</li><li>SERVICES</li><li>COUPONS</li><li>FINANCING</li><li>TESTIMONIALS</li><li>SERVICE AREA</li><li>BLOG</li></ul>
  </nav>
  <div class="abs search"><svg width="15" height="15" viewBox="0 0 16 16" fill="none" stroke="#fff" stroke-width="2"><circle cx="6.5" cy="6.5" r="5"/><path d="M10.5 10.5L15 15"/></svg></div>
</header>

<section class="abs hero">
  <div class="abs mascot" role="img" aria-label="Cartoon technician mascot giving a thumbs up and holding a thermometer"></div>
  <h1 class="abs">QUALITY GUARANTEED</h1>
  <p class="abs tag">Timeliness, competitive pricing, and skilled craftsmanship.</p>
  <form class="abs quick-form">
    <h2>QUICK CONTACT FORM</h2>
    <p class="intro">Mauris accumsan eros eget libero posuere vulputate. Etiam elit elit, elementum.</p>
    <div class="field" style="top:130px">Name</div>
    <div class="field" style="top:165px">Email</div>
    <div class="field" style="top:200px">Phone</div>
    <div class="field" style="top:236px;height:80px">Message</div>
    <div class="submit">SUBMIT</div>
  </form>
</section>

<section class="why">
  <h2 class="abs sec-title" style="top:688px">WHY CHOOSE US</h2>
  <div class="abs feature" style="left:159px;top:792px">
    <svg width="26" height="26" viewBox="0 0 26 26" fill="none" stroke="#555" stroke-width="1.3"><circle cx="13" cy="13" r="11"/><text x="13" y="16" font-size="8" text-anchor="middle" fill="#555" stroke="none" font-family="Open Sans,sans-serif">24</text></svg>
    <h3>24/7 Emergency Available</h3>
    <p>Mauris accumsan eros eget libero posuere vulputate.<br>Etiam elit elit, elementum sed.</p>
  </div>
  <div class="abs feature" style="left:480px;top:792px">
    <svg width="26" height="26" viewBox="0 0 26 26" fill="none" stroke="#555" stroke-width="1.5"><path d="M4 22L16 10M10 4l12 12M18 4a4 4 0 0 0 4 4"/></svg>
    <h3>Expert and Professional</h3>
    <p>Mauris accumsan eros eget libero posuere vulputate.<br>Etiam elit elit, elementum sed.</p>
  </div>
  <div class="abs feature" style="left:789px;top:792px">
    <svg width="26" height="26" viewBox="0 0 26 26" fill="none" stroke="#555" stroke-width="1.3"><circle cx="13" cy="13" r="11"/><text x="13" y="16" font-size="8" text-anchor="middle" fill="#555" stroke="none" font-family="Open Sans,sans-serif">24</text></svg>
    <h3>24/7 Emergency Available</h3>
    <p>Mauris accumsan eros eget libero posuere vulputate.<br>Etiam elit elit, elementum sed.</p>
  </div>
  <div class="abs feature" style="left:159px;top:940px">
    <svg width="26" height="28" viewBox="0 0 26 28" fill="none" stroke="#555" stroke-width="1.4"><circle cx="13" cy="10" r="7"/><path d="M8 16l-2 10 7-4 7 4-2-10"/></svg>
    <h3>Satisfaction Guarantee</h3>
    <p>Mauris accumsan eros eget libero posuere vulputate.<br>Etiam elit elit, elementum sed.</p>
  </div>
  <div class="abs feature" style="left:480px;top:938px">
    <svg width="28" height="26" viewBox="0 0 28 26" fill="none" stroke="#555" stroke-width="1.4"><circle cx="14" cy="13" r="11"/><path d="M6 13q8-7 16 0q-8 7-16 0z"/><circle cx="14" cy="13" r="2"/></svg>
    <h3>Free Inspection for site</h3>
    <p>Mauris accumsan eros eget libero posuere vulputate.<br>Etiam elit elit, elementum sed.</p>
  </div>
  <div class="abs feature" style="left:789px;top:940px">
    <svg width="26" height="28" viewBox="0 0 26 28" fill="none" stroke="#555" stroke-width="1.4"><circle cx="13" cy="10" r="7"/><path d="M8 16l-2 10 7-4 7 4-2-10"/></svg>
    <h3>Satisfaction Guarantee</h3>
    <p>Mauris accumsan eros eget libero posuere vulputate.<br>Etiam elit elit, elementum sed.</p>
  </div>
</section>

<section class="abs services">
  <h2 class="abs sec-title light" style="top:50px">OUR SERVICES</h2>
  <div class="abs card" style="left:180px;top:138px"><div class="photo" role="img" aria-label="Outdoor air conditioning condenser units" style="background:linear-gradient(180deg,#8fb6e0,#c9ccd0)"></div><h3>AIR CONDITIONG</h3></div>
  <div class="abs card" style="left:472px;top:138px"><div class="photo" role="img" aria-label="Furnace burners with blue flames" style="background:linear-gradient(180deg,#3b6fd8,#6d7a86)"></div><h3>HEATING</h3></div>
  <div class="abs card" style="left:764px;top:138px"><div class="photo" role="img" aria-label="Metal ductwork and pipes" style="background:linear-gradient(180deg,#a8adb3,#5f666e)"></div><h3>DUCT</h3></div>
  <div class="abs card" style="left:180px;top:363px"><div class="photo" role="img" aria-label="Heat pump unit on a wooden deck" style="background:linear-gradient(180deg,#5a5a58,#a07a58)"></div><h3>HEAT PUMP</h3></div>
  <div class="abs card" style="left:472px;top:363px"><div class="photo" role="img" aria-label="Air handler units in a mechanical room" style="background:linear-gradient(180deg,#7aa6d6,#a9a89a)"></div><h3>AIR HANDLER</h3></div>
  <div class="abs card" style="left:764px;top:363px"><div class="photo" role="img" aria-label="Hand installing an air filter" style="background:linear-gradient(180deg,#3a3a3a,#b99a62)"></div><h3>AIR CLEANERS</h3></div>
</section>

<section class="testimonials">
  <h2 class="abs sec-title" style="top:1800px">HAPPY CUSTOMER SAYS</h2>
  <article class="abs review" style="left:220px;top:1899px">
    <span class="who">Carla Weston</span>
    <p>Mauris accumsan eros eget libero posuere vulputate. Etiam elit elit, elementum sed varius at, adipiscing vitae est. Sed nec felis pellentesque, lacinia dui sed, ultricies sapien. Mauris accumsan eros eget libero posuere vulputate. Etiam elit elit, elementum sed varius.</p>
  </article>
  <div class="abs avatar" style="left:174px;top:1949px" role="img" aria-label="Customer portrait"></div>
  <article class="abs review" style="left:657px;top:1899px">
    <span class="who">Daniel Reyes</span>
    <p>Mauris accumsan eros eget libero posuere vulputate. Etiam elit elit, elementum sed varius at, adipiscing vitae est. Sed nec felis pellentesque, lacinia dui sed, ultricies sapien. Mauris accumsan eros eget libero posuere vulputate. Etiam elit elit, elementum sed varius.</p>
  </article>
  <div class="abs avatar" style="left:612px;top:1949px" role="img" aria-label="Customer portrait"></div>
</section>

<section class="abs cities">
  <h2 class="abs sec-title" style="top:50px">CITIES WE SERVE</h2>
  <p class="abs intro">Mauris accumsan eros eget libero posuere vulputate. Etiam elit elit, elementum sed varius at, adipiscing vitae est.</p>
  <ul class="abs city-list" style="left:159px;top:195px">
    <li><svg width="11" height="10" viewBox="0 0 11 10"><path d="M1 5l3 3 6-7" fill="none" stroke="#26923f" stroke-width="2"/></svg>California</li>
    <li><svg width="11" height="10" viewBox="0 0 11 10"><path d="M1 5l3 3 6-7" fill="none" stroke="#26923f" stroke-width="2"/></svg>Florid</li>
    <li><svg width="11" height="10" viewBox="0 0 11 10"><path d="M1 5l3 3 6-7" fill="none" stroke="#26923f" stroke-width="2"/></svg>Illinois</li>
    <li><svg width="11" height="10" viewBox="0 0 11 10"><path d="M1 5l3 3 6-7" fill="none" stroke="#26923f" stroke-width="2"/></svg>New Mexico</li>
    <li><svg width="11" height="10" viewBox="0 0 11 10"><path d="M1 5l3 3 6-7" fill="none" stroke="#26923f" stroke-width="2"/></svg>New York</li>
  </ul>
  <ul class="abs city-list" style="left:331px;top:195px">
    <li><svg width="11" height="10" viewBox="0 0 11 10"><path d="M1 5l3 3 6-7" fill="none" stroke="#26923f" stroke-width="2"/></svg>Washington</li>
    <li><svg width="11" height="10" viewBox="0 0 11 10"><path d="M1 5l3 3 6-7" fill="none" stroke="#26923f" stroke-width="2"/></svg>Indiana</li>
    <li><svg width="11" height="10" viewBox="0 0 11 10"><path d="M1 5l3 3 6-7" fill="none" stroke="#26923f" stroke-width="2"/></svg>Kentucky</li>
    <li><svg width="11" height="10" viewBox="0 0 11 10"><path d="M1 5l3 3 6-7" fill="none" stroke="#26923f" stroke-width="2"/></svg>Maryland</li>
    <li><svg width="11" height="10" viewBox="0 0 11 10"><path d="M1 5l3 3 6-7" fill="none" stroke="#26923f" stroke-width="2"/></svg>Nevad</li>
  </ul>
  <div class="abs van" role="img" aria-label="Branded company service van with mascot livery"></div>
</section>

<footer>
  <div class="abs footer">
    <div class="abs" style="left:168px;top:32px;width:245px">
      <h4>ABOUT US</h4>
      <p>We have been operating since the year 1998, serving the community across GTA. Lumera Optical offers a unique combination of affordable eyewear, personalized service as well as qualified and experienced staff. Lumera Optical is fully capable of rendering complete ........</p>
    </div>
    <div class="abs" style="left:503px;top:32px;width:260px">
      <h4>USEFUL LINKS</h4>
      <div style="display:flex;gap:60px">
        <ul class="links"><li>Home</li><li>About us</li><li>Contact Lens</li><li>Eye Glasses</li><li>Promotion</li></ul>
        <ul class="links"><li>Email us</li><li>Store Locations</li><li>Contact</li></ul>
      </div>
      <div class="f-social" style="margin-top:12px"><span></span><span></span><span></span><span></span><span></span></div>
    </div>
    <div class="abs" style="left:806px;top:32px;width:238px">
      <h4>NEWSLETTER</h4>
      <p>Nunc pellentesque semper ultrices. Pellentesque mollis faucibus anteNunc pellentesque semper ultrices. Pellentesque mollis faucibus</p>
      <div class="news-input">E-Mail</div>
      <div class="news-btn">SUBSCRIBE</div>
    </div>
  </div>
  <div class="abs copy">Copyrights © 2016 Brovik Climate Services. | All rights reserved</div>
</footer>

</body>
</html>
```